Brightwave Business Card

Professional Business Card Design required using the attached contact information.

Contact information can be rearranged as required.

The company is a new start up venture developing solar systems, the branding should be in keeping with that of one of the investors whose website is as follows https://www.quorvex.com/

```html
<!DOCTYPE html>
<html lang="en">
<head>
<meta charset="utf-8">
<title>Brightwave Renewables – Business Card</title>
<link rel="stylesheet" href="https://fonts.googleapis.com/css2?family=Montserrat:wght@400;500&display=swap">
<style>
  :root {
    --page: #fdfdfd;
    --slate: #323742;
    --slate-green: #2d4f4a;
    --brand-green: #2a6a58;
    --ink: #333333;
    --gold: #c9a45c;
    --white: #ffffff;
    --edge: #5a5770;
  }
  * { box-sizing: border-box; margin: 0; padding: 0; }
  html, body { width: 1059px; height: 1200px; overflow: hidden; background: var(--page); }
  body { position: relative; font-family: "Montserrat", sans-serif; }

  .card { position: absolute; left: 228px; width: 604px; height: 340px; overflow: hidden; }

  .card-front {
    top: 227px;
    background: linear-gradient(to bottom, var(--slate) 0%, var(--slate) 30%, var(--slate-green) 100%);
  }
  .wordmark {
    position: absolute; left: 0; right: 0; text-align: center;
    font-weight: 500; text-transform: uppercase; letter-spacing: 3.2px; white-space: nowrap;
  }
  .card-front .wordmark { top: 387px; top: 160px; font-size: 21px; color: var(--white); }

  .card-back { top: 628px; border: 1px solid var(--edge); background: var(--white); }
  .card-back .wordmark { top: 75px; font-size: 21px; color: var(--ink); }
  .holder-name {
    position: absolute; top: 118px; left: 0; right: 0; text-align: center;
    font-size: 24px; font-weight: 400; color: var(--brand-green); letter-spacing: 0.3px;
  }
  .contact-band {
    position: absolute; left: 0; right: 0; top: 173px; bottom: 0; background: var(--brand-green);
  }
  .contact-list { position: absolute; left: 120px; top: 24px; list-style: none; color: var(--white); font-size: 16px; line-height: 24px; letter-spacing: 0.2px; }
  .contact-list li { position: relative; padding-left: 21px; white-space: nowrap; }
  .contact-list .icon { position: absolute; left: 0; top: 5px; width: 14px; height: 14px; }
</style>
</head>
<body>
  <section class="card card-front" aria-label="Card front">
    <p class="wordmark">Brightwave Renewables</p>
  </section>

  <section class="card card-back" aria-label="Card back">
    <p class="wordmark">Brightwave Renewables</p>
    <h1 class="holder-name">Daniel Hollis</h1>
    <div class="contact-band">
      <ul class="contact-list">
        <li>
          <svg class="icon" viewBox="0 0 14 14" aria-hidden="true"><path d="M7 0.5a4.6 4.6 0 0 0-4.6 4.6C2.4 8.6 7 13.5 7 13.5s4.6-4.9 4.6-8.4A4.6 4.6 0 0 0 7 .5zm0 6.6a2 2 0 1 1 0-4 2 2 0 0 1 0 4z" fill="var(--gold)"/></svg>
          Brightwave Renewables LLC
        </li>
        <li>218 Harbor Street, Portland, ME 04101</li>
        <li>
          <svg class="icon" viewBox="0 0 14 14" aria-hidden="true"><path d="M3.2 1l2 2.6-1.1 1.5c.8 1.8 2.2 3.2 4 4l1.5-1.1L12.2 10l-1.2 2.4C6 12.2 1.8 8 1.6 3z" fill="var(--gold)"/><path d="M8 1.5a4.5 4.5 0 0 1 4.5 4.5M8 3.5A2.5 2.5 0 0 1 10.5 6" stroke="var(--gold)" stroke-width="1.1" fill="none"/></svg>
          Direct: +1 (555) 014-2276
        </li>
        <li>
          <svg class="icon" viewBox="0 0 14 14" aria-hidden="true"><path d="M7 0.5L12.5 5v8H1.5V5z" fill="var(--gold)"/><path d="M1.5 5L7 9l5.5-4M1.5 13l4-4M12.5 13l-4-4" stroke="var(--brand-green)" stroke-width="0.9" fill="none"/></svg>
          daniel.hollis@brightwave-renewables.com
        </li>
      </ul>
    </div>
  </section>
</body>
</html>
```